877 stay Bold

Redesigning this front and back business card flyer and keeping the info but making it look better.

This is all about using the info and logo on the business card design and creating a better layout using any of the following and more.

Changing the background color or imagine, chaining the placement of content, resizing content.

Target Market(s)

Targeting people that have been injured on one side and people that have been giving a DUI on the other.

Contact Information for Business Card

We are looking to keep the info but make it look a fee cleaner and less cluttered

Font styles to use
Sans Serif

Requirements
Must have
• Must have the same info but a better layout.
Nice to have
• better background colors or image or layout. different fonts or same font all design options that will make it look professional and clean.

```html
<!DOCTYPE html>
<html lang="en">
<head>
<meta charset="UTF-8">
<title>877 stay Bold – Business Card Front and Back</title>
<link rel="stylesheet" href="https://fonts.googleapis.com/css2?family=Open+Sans:wght@400;600;700;800&display=swap">
<style>
  :root {
    --ink: #111111;
    --charcoal: #353535;
    --paper: #f1f1f1;
    --red: #c0111a;
    --text-grey: #3c3c3c;
    --backdrop: #dcdcdc;
    --white: #ffffff;
  }
  * { box-sizing: border-box; margin: 0; padding: 0; }
  html, body {
    width: 1200px; height: 1200px; overflow: hidden;
    background: var(--backdrop);
    font-family: "Open Sans", Arial, sans-serif;
  }
  .card {
    position: absolute; left: 100px; width: 1000px; height: 540px;
    overflow: hidden; box-shadow: 0 10px 30px rgba(0,0,0,.18);
  }

  /* Shared vertical brand lockup */
  .brand-slot {
    position: absolute; display: flex; align-items: center; justify-content: center;
  }
  .brand-vertical {
    writing-mode: vertical-rl; transform: rotate(180deg);
    font-weight: 800; font-size: 40px; line-height: 1; color: var(--ink); white-space: nowrap;
    display: flex; align-items: center; gap: 12px;
  }
  .brand-vertical .brand-mark { width: 26px; height: 26px; background: var(--red); flex: none; }

  /* DUI side */
  .card-dui { top: 40px; background: var(--paper); }
  .dui-header {
    position: absolute; top: 0; left: 0; right: 0; height: 100px;
    background: var(--ink); color: var(--white);
    display: flex; align-items: center; justify-content: flex-end;
    padding-right: 50px;
    font-size: 54px; font-weight: 600; letter-spacing: 2px; text-transform: uppercase;
  }
  .dui-header-rule {
    position: absolute; top: 108px; left: 0; right: 0; height: 5px; background: var(--red);
  }
  .card-dui .brand-slot { left: 40px; width: 110px; top: 130px; bottom: 50px; }
  .dui-content { position: absolute; left: 200px; top: 150px; right: 50px; }
  .dui-question { color: var(--red); font-size: 28px; font-weight: 700; margin-bottom: 12px; }
  .tip-list { list-style: none; color: var(--text-grey); font-size: 24px; line-height: 1.32; }
  .tip-list li { position: relative; padding-left: 24px; }
  .tip-list li::before {
    content: ""; position: absolute; left: 0; top: 12px; width: 10px; height: 10px; background: var(--red);
  }
  .tip-list li.continued::before { display: none; }
  .dui-footer-rule { position: absolute; left: 0; right: 0; bottom: 26px; height: 5px; background: var(--red); }
  .dui-footer-line { position: absolute; left: 0; right: 0; bottom: 16px; height: 4px; background: var(--ink); }

  /* Injury side */
  .card-injury { top: 620px; background: var(--charcoal); }
  .injury-brand-panel { position: absolute; left: 0; top: 0; bottom: 0; width: 190px; background: var(--paper); }
  .injury-brand-panel .brand-slot { left: 0; right: 0; top: 40px; bottom: 40px; }
  .red-bar { position: absolute; top: 0; bottom: 0; width: 12px; background: var(--red); }
  .red-bar.left { left: 190px; }
  .red-bar.right { left: 790px; }
  .slogan-panel {
    position: absolute; left: 802px; top: 0; bottom: 0; width: 140px; background: var(--paper);
    display: flex; align-items: center; justify-content: center;
  }
  .slogan {
    writing-mode: vertical-rl; transform: rotate(180deg);
    color: var(--red); font-size: 30px; font-weight: 700; line-height: 1.25; text-align: center;
  }
  .injury-content { position: absolute; left: 232px; top: 28px; width: 540px; color: var(--white); }
  .injury-lead { font-size: 38px; font-weight: 400; }
  .injury-headline {
    color: var(--red); font-size: 70px; font-weight: 700; line-height: 1; text-transform: uppercase; margin: 2px 0 10px;
  }
  .reason-list { list-style: none; font-size: 24px; line-height: 1.3; }
  .reason-list li { position: relative; padding-left: 22px; }
  .reason-list li::before {
    content: ""; position: absolute; left: 0; top: 12px; width: 10px; height: 10px; background: var(--red);
  }
  .photo-row { display: flex; gap: 10px; margin: 16px 0 14px; }
  .photo { width: 170px; height: 96px; }
  .photo-crash { background: linear-gradient(135deg, #2a1a22, #7a6a78 55%, #3a2a30); }
  .photo-wheelchair { background: linear-gradient(135deg, #1b1f24, #4a5058 60%, #2a2e33); }
  .photo-crutches { background: linear-gradient(135deg, #9a9590, #c8c2bb 55%, #4a4f5a); }
  .contact-call { font-size: 24px; font-weight: 700; letter-spacing: .5px; }
  .contact-web { font-size: 22px; font-weight: 400; }
</style>
</head>
<body>

<section class="card card-dui">
  <div class="dui-header">Stay Bold After a DUI</div>
  <div class="dui-header-rule"></div>
  <div class="brand-slot">
    <div class="brand-vertical"><span class="brand-mark"></span>877 STAY BOLD</div>
  </div>
  <div class="dui-content">
    <h2 class="dui-question">What should I do if I get pulled over for DUI?</h2>
    <ul class="tip-list">
      <li>Pull over in a calm, normal manner</li>
      <li>Be polite at all times</li>
      <li>Do not admit to drinking</li>
      <li>Do not submit to any field sobriety tests</li>
      <li>Do not submit to talking a chemical test</li>
      <li class="continued">( breath, blood, or urine )</li>
      <li>Do not make any statement after being arrested,</li>
      <li class="continued">Especially when placed in the police cruiser</li>
    </ul>
  </div>
  <div class="dui-footer-rule"></div>
  <div class="dui-footer-line"></div>
</section>

<section class="card card-injury">
  <div class="injury-brand-panel">
    <div class="brand-slot">
      <div class="brand-vertical"><span class="brand-mark"></span>877 STAY BOLD</div>
    </div>
  </div>
  <div class="red-bar left"></div>
  <div class="injury-content">
    <p class="injury-lead">If You’ve Been Injured</p>
    <h2 class="injury-headline">Stay Bold</h2>
    <ul class="reason-list">
      <li>For an inexperienced lawyer!</li>
      <li>For less than you deserve!</li>
      <li>For paying massive medical bills!</li>
      <li>For a life of pain and debt!</li>
    </ul>
    <div class="photo-row">
      <div class="photo photo-crash" role="img" aria-label="Photo of a damaged car at a night-time accident scene"></div>
      <div class="photo photo-wheelchair" role="img" aria-label="Photo of a person in a wheelchair by a window"></div>
      <div class="photo photo-crutches" role="img" aria-label="Photo of a leg in a walking boot with crutches"></div>
    </div>
    <p class="contact-call">CALL 877-782-9265</p>
    <p class="contact-web">www.877StayBold.com</p>
  </div>
  <div class="red-bar right"></div>
  <div class="slogan-panel">
    <p class="slogan">We Fight For You, So You<br>Can Focus On Getting Better</p>
  </div>
</section>

</body>
</html>
```